Graphic Design Set for Banner Ads - Sizes and Specs for Pixmora

We need a set of 6 ads of the following sizes created for Pixmora:

Medium rectangle: 300×250
Leaderboard: 728×90
Wide skyscraper: 160×600
Large rectangle: 300x600
Mobile leaderboard: 320×50

Here are the Formatting Guidelines (WEB ADS): https://help.pixmora.example/hc/en-us/articles/583920147-Ad-Content-and-Format-Guidelines

Here is the website: https://valmiraliving.example/

Here are some words for the ad - feel free to use creative liberties if you have something better or need less words.

1. The Future of Aging is Here

2. Dementia At-Home Care

3. Benefits of an Assisted Living from the Privacy of Your Home - link to

4. Idaho's New Senior Care Option

5. The Security of Senior Living from the Comfort of Your Home

I have the images for all website photos, if you need more images, please let me know.

Target Market(s)

Women age 55+

Industry/Entity Type

Graphic Design

Requirements
Must have
• Incorporate website imagery as much as possible
Should not have
• a feeling of helplessness, old, etc.

```html
<!DOCTYPE html>
<html lang="en">
<head>
<meta charset="utf-8">
<title>Valmira Living – Banner Ad Set</title>
<link rel="stylesheet" href="https://fonts.googleapis.com/css2?family=Roboto:wght@400;500&display=swap">
<style>
  :root{
    --canvas:#ece7e1;
    --brand-blue:#0099cc;
    --navy:#1c3d66;
    --white:#ffffff;
    --gold:#c8963a;
    --panel-grey:#f2f2f2;
    --photo-tone:#a7acab;
    --ink:#1f1f1f;
  }
  *{box-sizing:border-box;margin:0;padding:0}
  html,body{width:1200px;height:1075px;overflow:hidden;background:var(--canvas)}
  body{position:relative;font-family:"Roboto",Arial,sans-serif}
  .ad{position:absolute;background:var(--brand-blue);overflow:hidden}
  .ad svg.art{position:absolute;left:0;top:0}
  .art .panel{fill:var(--panel-grey)}
  .art .band{fill:var(--brand-blue)}
  .art .photo{fill:var(--photo-tone)}
  .art .edge{fill:none;stroke:var(--gold)}
  .brand{position:absolute;display:flex;align-items:center;gap:6px;color:var(--ink);font-weight:400;white-space:nowrap}
  .brand-dot{border-radius:50%;background:var(--gold);flex:none}
  .headline{position:absolute;text-align:center;line-height:1.15}
  .headline .lead{display:block;color:var(--navy);font-weight:400}
  .headline .main{display:block;color:var(--white);font-weight:500}
  .cta{position:absolute;display:flex;align-items:center;justify-content:center;border:2px solid var(--gold);color:var(--white);font-weight:400;letter-spacing:.06em;text-transform:uppercase}

  .ad--leaderboard{left:77px;top:76px;width:907px;height:110px}
  .ad--large-rect{left:77px;top:240px;width:373px;height:748px}
  .ad--skyscraper{left:501px;top:240px;width:198px;height:748px}
  .ad--medium-rect{left:751px;top:240px;width:373px;height:310px;background:var(--panel-grey)}
  .ad--mobile{left:751px;top:602px;width:398px;height:59px}
</style>
</head>
<body>

<section class="ad ad--leaderboard" aria-label="Leaderboard ad">
  <svg class="art" width="907" height="110" viewBox="0 0 907 110">
    <rect class="panel" x="0" y="0" width="162" height="110"/>
    <path class="photo" role="img" aria-label="Photo: senior woman doing a yoga pose on a mat by a lake" d="M160 0H360Q378 55 360 110H160Z"/>
    <path class="edge" d="M360 0Q378 55 360 110" stroke-width="3"/>
  </svg>
  <div class="brand" style="left:14px;top:44px;font-size:19px"><span class="brand-dot" style="width:10px;height:10px"></span>Valmira Living</div>
  <div class="headline" style="left:390px;width:300px;top:10px"><span class="lead" style="font-size:33px">Idaho's New</span><span class="main" style="font-size:33px">Senior Care Option</span></div>
  <div class="cta" style="left:729px;top:38px;width:149px;height:36px;font-size:15px">Learn More</div>
</section>

<section class="ad ad--large-rect" aria-label="Large rectangle ad">
  <svg class="art" width="373" height="748" viewBox="0 0 373 748">
    <path class="panel" d="M0 0H373V116Q186 84 0 116Z"/>
    <path class="photo" role="img" aria-label="Photo: senior woman doing a yoga pose on a mat by a lake" d="M0 116Q186 84 373 116V370Q186 396 0 370Z"/>
    <path class="edge" d="M0 116Q186 84 373 116" stroke-width="3"/>
    <path class="edge" d="M0 370Q186 396 373 370" stroke-width="3"/>
  </svg>
  <div class="brand" style="left:0;width:373px;justify-content:center;top:30px;font-size:30px"><span class="brand-dot" style="width:14px;height:14px"></span>Valmira Living</div>
  <div class="headline" style="left:0;width:373px;top:414px;line-height:1.43"><span class="lead" style="font-size:35px">Idaho's New</span><span class="main" style="font-size:35px">Senior Care Option</span></div>
  <div class="cta" style="left:100px;top:572px;width:173px;height:48px;font-size:17px">Learn More</div>
</section>

<section class="ad ad--skyscraper" aria-label="Wide skyscraper ad">
  <svg class="art" width="198" height="748" viewBox="0 0 198 748">
    <path class="panel" d="M0 0H198V129Q99 105 0 129Z"/>
    <path class="photo" role="img" aria-label="Photo: senior woman doing a yoga pose on a mat by a lake" d="M0 129Q99 105 198 129V329Q99 335 0 329Z"/>
    <path class="edge" d="M0 129Q99 105 198 129" stroke-width="3"/>
    <path class="edge" d="M0 329Q99 335 198 329" stroke-width="3"/>
  </svg>
  <div class="brand" style="left:0;width:198px;justify-content:center;top:36px;font-size:21px"><span class="brand-dot" style="width:10px;height:10px"></span>Valmira Living</div>
  <div class="headline" style="left:0;width:198px;top:370px;line-height:1.45"><span class="lead" style="font-size:27px">Idaho's New</span><span class="main" style="font-size:27px">Senior Care<br>Option</span></div>
  <div class="cta" style="left:25px;top:560px;width:149px;height:36px;font-size:15px">Learn More</div>
</section>

<section class="ad ad--medium-rect" aria-label="Medium rectangle ad">
  <svg class="art" width="373" height="310" viewBox="0 0 373 310">
    <path class="band" d="M0 64Q90 52 176 56Q166 180 180 310H0Z"/>
    <path class="photo" role="img" aria-label="Photo: senior woman doing a yoga pose on a mat by a lake" d="M178 0Q164 155 180 310H373V0Z"/>
    <path class="edge" d="M178 0Q164 155 180 310" stroke-width="3"/>
  </svg>
  <div class="brand" style="left:0;width:174px;justify-content:center;top:14px;font-size:17px"><span class="brand-dot" style="width:9px;height:9px"></span>Valmira Living</div>
  <div class="headline" style="left:0;width:168px;top:90px;line-height:1.45"><span class="lead" style="font-size:22px">Idaho's New</span><span class="main" style="font-size:22px">Senior Care<br>Option</span></div>
  <div class="cta" style="left:11px;top:241px;width:149px;height:35px;font-size:15px">Learn More</div>
</section>

<section class="ad ad--mobile" aria-label="Mobile leaderboard ad">
  <svg class="art" width="398" height="59" viewBox="0 0 398 59">
    <rect class="panel" x="0" y="0" width="100" height="59"/>
    <path class="photo" role="img" aria-label="Photo: senior woman doing a yoga pose on a mat by a lake" d="M99 0H196Q205 30 196 59H99Z"/>
    <path class="edge" d="M196 0Q205 30 196 59" stroke-width="2"/>
  </svg>
  <div class="brand" style="left:6px;top:21px;font-size:12px;gap:4px"><span class="brand-dot" style="width:6px;height:6px"></span>Valmira Living</div>
  <div class="headline" style="left:205px;width:193px;top:8px;font-size:13px;white-space:nowrap"><span class="lead" style="display:inline">Idaho's New </span><span class="main" style="display:inline">Senior Care Option</span></div>
  <div class="cta" style="left:251px;top:30px;width:94px;height:24px;font-size:10px;border-width:1.5px">Learn More</div>
</section>
</body>
</html>
```